Birchfield Yardworks Complete Garden & Lawn Care

I will upload a flyer, I wanna pretty much same, please change the logo and I will upload description of the job I offer soon
Gonna be in A5 size, and I would like like double sides
I would like something creative and modern to impress the clients, I upload my business card as well, on flyer need to have my business card information
TRELBIX IS ONLY A SAMPLE FLYER AND PLEASE I DONT WANT TO SEE IT IN MY FLYERS, Thanks
Updates
on small lines instead of 6 months I would like 3 months
Target Market(s)
Residentials and commercials
Industry/Entity Type
Business
Look and feel
Each slider illustrates characteristics of the customer's brand and the style your logo design should communicate.

```html
<!DOCTYPE html>
<html lang="en">
<head>
<meta charset="utf-8">
<title>Birchfield Yardworks – Lawn Mowing Flyer</title>
<link rel="stylesheet" href="https://fonts.googleapis.com/css2?family=Anton&family=Open+Sans:wght@400;600;700;800&display=swap">
<style>
  :root {
    --green-dark: #1b6d3a;
    --green-light: #8bbd3f;
    --green-brand: #3f9a3b;
    --yellow: #f4ef7c;
    --navy: #3d3a6c;
    --ink: #111111;
    --grey: #555555;
    --white: #ffffff;
  }
  * { margin: 0; padding: 0; box-sizing: border-box; }
  html, body { width: 846px; height: 1200px; overflow: hidden; background: var(--white); }
  .flyer {
    position: relative; width: 846px; height: 1200px; overflow: hidden;
    background: var(--white);
    font-family: "Open Sans", Arial, sans-serif;
  }
  .abs { position: absolute; }

  /* Brand */
  .brand { left: 34px; top: 120px; display: flex; align-items: center; gap: 14px; }
  .brand-dot { width: 34px; height: 34px; border-radius: 50%; background: var(--green-brand); flex: none; }
  .brand-name { font-family: "Open Sans", Arial, sans-serif; font-weight: 700; font-size: 34px; color: var(--green-brand); letter-spacing: 1px; white-space: nowrap; }
  .brand-tag { left: 34px; top: 214px; font-size: 19px; color: var(--grey); letter-spacing: 1.5px; font-weight: 600; }

  /* Badge */
  .badge { left: 580px; top: 28px; width: 250px; height: 214px; }

  /* Offer band */
  .offer { left: 0; top: 276px; width: 846px; height: 192px; background: var(--green-dark); }
  .offer-headline {
    position: absolute; left: 0; top: 8px; width: 846px; text-align: center;
    font-family: "Anton", Impact, sans-serif; color: var(--yellow);
    font-size: 57px; line-height: 60px; letter-spacing: 3.5px;
  }
  .offer-sub {
    position: absolute; left: 131px; top: 132px;
    font-weight: 700; font-size: 30px; color: var(--white); white-space: nowrap;
  }

  /* Services */
  .services { left: 0; top: 492px; width: 846px; height: 398px; background: var(--green-light); }
  .service-main { position: absolute; left: 19px; font-weight: 700; font-size: 22.5px; color: var(--ink); white-space: nowrap; }
  .service-dash { position: absolute; left: 410px; width: 20px; height: 2px; background: var(--ink); }
  .service-detail { position: absolute; left: 452px; font-weight: 700; font-size: 18.5px; line-height: 25px; color: var(--ink); }
  .placeholder {
    position: absolute; left: 0; top: 272px; width: 804px; text-align: center;
    font-weight: 600; font-size: 22.5px; line-height: 25px; color: var(--ink);
  }

  /* Contact */
  .contact-band { left: 0; top: 890px; width: 846px; height: 200px; }
  .contact-names { left: 27px; top: 910px; font-size: 40px; font-weight: 600; color: var(--white); white-space: nowrap; }
  .contact-lines { left: 392px; top: 900px; font-size: 23.5px; line-height: 41px; font-weight: 600; color: var(--white); white-space: nowrap; }
  .call-now { left: 0; top: 1066px; width: 846px; text-align: center; font-weight: 800; font-size: 57px; color: var(--navy); letter-spacing: 1px; white-space: nowrap; }
</style>
</head>
<body>
<main class="flyer">

  <header class="abs brand">
    <span class="brand-dot"></span>
    <span class="brand-name">Birchfield Yardworks</span>
  </header>
  <p class="abs brand-tag">Complete Garden &amp; Lawn Care</p>

  <svg class="abs badge" viewBox="0 0 250 214" aria-label="Value guaranteed, 100% locally owned and operated">
    <polygon fill="var(--navy)" points="125,0 139,28 162,6 168,38 196,22 192,55 226,49 210,78 246,84 220,106 248,126 214,138 236,166 200,166 206,200 174,186 164,214 142,192 125,214 108,192 86,214 76,186 44,200 50,166 14,166 36,138 2,126 30,106 4,84 40,78 24,49 58,55 54,22 82,38 88,6 111,28"/>
    <text x="125" y="108" text-anchor="middle" font-family="Anton, Impact, sans-serif" font-size="48" fill="var(--white)" letter-spacing="2">VALUE</text>
    <text x="125" y="130" text-anchor="middle" font-family="Anton, Impact, sans-serif" font-size="17" fill="var(--yellow)" letter-spacing="1">GUARANTEED!</text>
    <text x="125" y="144" text-anchor="middle" font-family="Open Sans, Arial, sans-serif" font-weight="800" font-size="8" fill="var(--white)">100% LOCALLY OWNED OPERATED</text>
  </svg>

  <section class="abs offer">
    <h1 class="offer-headline">We’ll beat your current<br>Lawn mowing rate by 10%</h1>
    <p class="offer-sub">New price guaranteed for 3 months</p>
  </section>

  <section class="abs services">
    <p class="service-main" style="top:38px">Residential &amp; Commercial</p>
    <p class="service-main" style="top:75px">Complete Lawn &amp; garden care</p>
    <p class="service-main" style="top:124px">High Pressure cleaning</p>
    <p class="service-main" style="top:168px">Section cleaning</p>
    <p class="service-main" style="top:211px">Trailer Loads</p>

    <span class="service-dash" style="top:60px"></span>
    <p class="service-detail" style="top:47px">Obligation free quotes</p>
    <span class="service-dash" style="top:91px"></span>
    <p class="service-detail" style="top:78px">garden spraying, weed spraying,<br>landscaping, mulching.</p>
    <span class="service-dash" style="top:150px"></span>
    <p class="service-detail" style="top:137px">Gutters &amp; paths</p>
    <span class="service-dash" style="top:187px"></span>
    <p class="service-detail" style="top:174px">Property vacates</p>
    <span class="service-dash" style="top:214px"></span>
    <p class="service-detail" style="top:201px">General handyman jobs</p>

    <p class="placeholder">Some text to come here this area.....<br>Some text to come here this area.....<br>Some text to come here this area.....<br>Some text to come here this area.....</p>
  </section>

  <svg class="abs contact-band" viewBox="0 0 846 200" aria-hidden="true">
    <rect x="0" y="0" width="846" height="200" fill="var(--green-dark)"/>
    <path d="M0 170 Q330 62 846 98 V200 H0 Z" fill="var(--white)"/>
  </svg>
  <p class="abs contact-names">Daniel / Marcus</p>
  <p class="abs contact-lines">Phone: 0400 555 127<br>Email: admin@birchfieldyards.com.au</p>

  <p class="abs call-now">CALL NOW: 0400 555 384</p>

</main>
</body>
</html>
```